Webpage layout and company logo combination

We are trying to renovate an existing site to make it sharper and sophisticated in appearance. This is the existing site: http://www.kestrelhomesnj.com/agents.html . The new presentation should be bright, sharp, sophisticated and should incorporate two additional menu tabs. The menu tabs will be revised as follows: Property Listings, Property Management, Advisory & Consulting, Local Info, R/E Tools, Our Team (please disregard Korean language characters, which will be installed after English version is completed, separately).

It Company

```html
<!DOCTYPE html>
<html lang="en">
<head>
<meta charset="utf-8">
<title>Kestrel Homes</title>
<link href="https://fonts.googleapis.com/css2?family=Open+Sans:wght@300;400;600;700&display=swap" rel="stylesheet">
<style>
:root{
  --sage:#bfc597;
  --olive:#5c5428;
  --olive-dark:#3e3716;
  --maroon:#6d2b38;
  --nav-active:#7b2d37;
  --ink:#333;
  --white:#fff;
  --footer:#5d5428;
  --footer-text:#efeddc;
}
*{margin:0;padding:0;box-sizing:border-box}
html,body{width:716px;height:1200px;overflow:hidden}
body{font-family:"Open Sans",Arial,sans-serif;background:var(--sage);color:var(--ink);position:relative}
.abs{position:absolute}
.header{left:0;top:0;width:716px;height:58px;background:var(--sage)}
.brand{left:67px;top:20px;display:flex;align-items:center;gap:7px;font-size:20px;font-weight:700;color:var(--maroon)}
.brand-mark{width:18px;height:18px;background:var(--maroon)}
.lang{right:77px;top:40px;font-size:8.5px;color:#222}
.nav{left:0;top:58px;width:716px;height:35px;background:linear-gradient(#6a5f2d,var(--olive-dark))}
.nav a{position:absolute;top:9px;color:var(--white);font-size:9.2px;text-decoration:none;line-height:11px}
.nav a.active{background:var(--nav-active);padding:4px 6px;top:5px}
.hero{left:0;top:93px;width:716px;height:226px;background:linear-gradient(100deg,#1a1a1c 0%,#2f3236 35%,#8a8a88 60%,#d4d4d2 85%,#eeeeec 100%)}
.dots{left:326px;top:302px;display:flex;gap:4px}
.dots span{width:8px;height:8px;border-radius:50%;background:#eee}
.dots span:first-child{background:#c7cca0}
.panel{left:72px;top:332px;width:572px;height:710px;background:var(--white)}
h2{font-weight:400;font-size:14.5px;color:var(--maroon)}
.welcome{left:77px;top:343px;width:322px}
.welcome p{font-size:7.9px;line-height:14.4px;margin-top:10px;color:#444;hyphens:auto;-webkit-hyphens:auto}
.welcome p+p{margin-top:14px}
.videos{left:411px;top:343px}
.video{left:411px;top:379px;width:227px;height:135px;background:#d9dad6;padding:4px}
.video-frame{width:100%;height:100%;background:linear-gradient(90deg,#eef0ea,#c9cfc0 55%,#9ea58e)}
.play{left:508px;top:434px;width:35px;height:21px;background:#222;border-radius:3px}
.play::after{content:"";position:absolute;left:14px;top:5px;border-left:9px solid #fff;border-top:5.5px solid transparent;border-bottom:5.5px solid transparent}
.video-bar{left:423px;top:494px;width:208px;height:8px;background:#1d2a33}
.video-bar i{position:absolute;left:3px;top:2px;width:44px;height:4px;background:#2b9ad6}
.section-bar{left:78px;width:560px;height:34px;background:var(--olive);color:var(--white);font-size:11px;padding:10px 0 0 10px}
.select{left:486px;top:559px;width:148px;height:19px;background:var(--olive-dark);color:var(--white);font-size:8.5px;padding:4px 8px}
.listing{top:606px;width:131px;font-size:7.9px;color:#444}
.listing .photo{height:87px}
.listing .loc{margin-top:6px}
.listing .desc{margin-top:14px;line-height:14.4px;hyphens:auto;-webkit-hyphens:auto;height:58px;overflow:hidden}
.listing .mls{margin-top:11px}
.listing .price{font-size:16px;font-weight:300;color:#333;line-height:20px}
.listing .more{margin-top:1px}
b{font-weight:700;color:#333}
.agent-photo{left:78px;top:939px;width:84px;height:63px;background:linear-gradient(#b9c3cc,#7a6a5a 60%,#5b3a2a)}
.agent{font-size:8.1px;line-height:14.4px;color:#222}
.agent .name{font-weight:700;color:var(--maroon);font-size:8.3px}
.footer{left:0;top:1042px;width:716px;height:158px;background:var(--footer)}
.fcol{font-size:8.5px;color:var(--footer-text);line-height:18px}
.social{left:528px;font-size:8.5px;color:var(--footer-text);display:flex;align-items:center;gap:22px}
.social i{width:19px;height:19px;border-radius:50%;background:var(--white);display:inline-block}
.copy{left:0;top:1172px;width:716px;text-align:center;font-size:8.3px;color:var(--footer-text)}
</style>
</head>
<body>
<header class="abs header"></header>
<div class="abs brand"><span class="brand-mark"></span>Kestrel Homes</div>
<div class="abs lang">Korean &nbsp;|&nbsp; English</div>
<nav class="abs nav">
  <a class="active" style="left:90px">Home</a>
  <a style="left:140px">Property Listings</a>
  <a style="left:226px">Property Management</a>
  <a style="left:336px">Advisory &amp; Consulting</a>
  <a style="left:442px">Local Info</a>
  <a style="left:502px">R/E Tools</a>
  <a style="left:561px">Our Team</a>
</nav>
<div class="abs hero" role="img" aria-label="Agent in a suit holding a small model house"></div>
<div class="abs dots"><span></span><span></span><span></span></div>

<main class="abs panel"></main>
<section class="abs welcome">
  <h2>Welcome to Kestrel Homes</h2>
  <p>Lorem Ipsum is simply dummy text of the printing and typesetting industry. Lorem Ipsum has been the industry's standard dummy text ever since the 1500s, when an unknown printer took a galley of type and scrambled it to make a type specimen book. It has survived not only five centuries, but also the leap into electronic typesetting, remaining essentially unchanged. It was popularised in the 1960s with the release of Letterset sheets containing Lorem Ipsum passages, and more recently with desktop publishing software like Folio PageCraft including versions of Lorem Ipsum.</p>
  <p>Lorem Ipsum is simply dummy text of the printing and typesetting industry. Lorem Ipsum has been the industry's standard dummy text ever since the 1500s,</p>
</section>
<h2 class="abs videos">Featured Videos</h2>
<div class="abs video"><div class="video-frame" role="img" aria-label="Video still of a couple in front of their new house"></div></div>
<div class="abs play"></div>
<div class="abs video-bar"><i></i></div>

<div class="abs section-bar" style="top:552px">Featured Listings</div>
<div class="abs select">Residential</div>

<article class="abs listing" style="left:78px">
  <div class="photo" role="img" aria-label="Townhouse community with landscaped lawn" style="background:linear-gradient(#cfdff0,#9fb08a 55%,#6e7f4c)"></div>
  <div class="loc"><b>Location:</b> Riverton, NJ</div>
  <div class="desc"><b>Description:</b> Harbor Point. Perfect blend of design, privacy and standard of living. River front community. Ashford model. Hardwood ...</div>
  <div class="mls">MLS ID: 1048273</div><div class="price">$625,000</div><div class="more"><b>More Details</b></div>
</article>
<article class="abs listing" style="left:221px">
  <div class="photo" role="img" aria-label="Brick two-storey house front" style="background:linear-gradient(#dfe6ea,#a4705a 40%,#7a4a38)"></div>
  <div class="loc"><b>Location:</b> Riverton, NJ</div>
  <div class="desc"><b>Description:</b> Harbor Point. Perfect blend of design, privacy and standard of living. River front community. Ashford model. Hardwood ...</div>
  <div class="mls">MLS ID: 1048273</div><div class="price">$625,000</div><div class="more"><b>More Details</b></div>
</article>
<article class="abs listing" style="left:364px">
  <div class="photo" role="img" aria-label="Atrium courtyard with plants seen from above" style="background:linear-gradient(120deg,#5b7a3a,#c8b48a 50%,#8e8e86)"></div>
  <div class="loc"><b>Location:</b> Riverton, NJ</div>
  <div class="desc"><b>Description:</b> Harbor Point. Perfect blend of design, privacy and standard of living. River front community. Ashford model. Hardwood ...</div>
  <div class="mls">MLS ID: 1048273</div><div class="price">$625,000</div><div class="more"><b>More Details</b></div>
</article>
<article class="abs listing" style="left:508px">
  <div class="photo" role="img" aria-label="Red brick house on a street" style="background:linear-gradient(#e6e8ec,#9b4a3e 50%,#8a8a88)"></div>
  <div class="loc"><b>Location:</b> Riverton, NJ</div>
  <div class="desc"><b>Description:</b> Harbor Point. Perfect blend of design, privacy and standard of living. River front community. Ashford model. Hardwood ...</div>
  <div class="mls">MLS ID: 1048273</div><div class="price">$625,000</div><div class="more"><b>More Details</b></div>
</article>

<div class="abs section-bar" style="top:894px">Our Agents</div>
<div class="abs agent-photo" role="img" aria-label="Broker portrait at his desk"></div>
<div class="abs agent" style="left:170px;top:935px"><div class="name">MARTIN VALE</div>Broker/Owner<br>Direct: 866-555-0140<br>Office: 201-555-0100<br>Cell: 201-555-0177<br>mvale@kestrelhomes.com</div>
<div class="abs agent" style="left:283px;top:937px"><div class="name">OWEN PARK</div>Sales Agent<br>Direct:<br>Office: (201)555-0100<br>Cell: (917)555-0162</div>
<div class="abs agent" style="left:393px;top:935px"><div class="name">DANIEL ROH</div>Sales Agent<br>Direct: (201)555-0123<br>Office: (201)555-0100<br>Cell: (201)555-0123</div>
<div class="abs agent" style="left:495px;top:932px"><div class="name">CLARA MOSS</div>Sales Agent<br>Direct:<br>Office: (201)555-0100<br>Cell: (201)555-0188</div>

<footer class="abs footer"></footer>
<div class="abs fcol" style="left:73px;top:1051px">Home<br>Property Listings<br>Property Management<br>Advisory &amp; Consulting<br>Local Info<br>R/E Tools<br>Our Team</div>
<div class="abs fcol" style="left:233px;top:1051px">Privacy Policy<br>Tems &amp; Conditions<br>Legal Conditions</div>
<div class="abs fcol" style="left:356px;top:1051px">410 Riverside Avenue,<br>Suite 210 Edgewater, NJ 07020<br>Tel (201)555-0100<br>Fax (201)555-0199</div>
<div class="abs social" style="top:1053px">Facepage <i></i></div>
<div class="abs social" style="top:1077px">Chirper <i style="margin-left:10px"></i></div>
<div class="abs copy">© 2014 Company Name ,All Rihts Reserved</div>
</body>
</html>
```